QV Holdings Website Redesign Contest

We want to refresh our website to be more insitutional, professional for an international audience. We have designed a new logo for this purpose and that has been attached. A full brand brief and positioning statement has also been attached. Please read through all the documents carefully before designing. The old website is found here: https://qv-holdings.example/

Target Market(s)

Actuaries and associated businesses internationally

Industry/Entity Type

professional services - actuaries

Number of Pages Required

3 page

Font styles to use
Sans Serif

Colors
0054AA
0677BA
7BADD7
CADEEF
E8F1F8
0094D4
00A9DD
6FCCEA
C7EBF8
E9F6FB
F0912C
F2A743
F7CA91
FBE8D2
FDF5EE
EE7325
F08F49
F5BC92
FAE3D3
FDF4ED
EB3D1F
EC4F4E
F09395
F8D3D4
FCEDEE

Requirements
Must have
• blues and greens to match the logo color, complimentary colors, navigation
Nice to have
• old site: https://qv-holdings.example/

```html
<!DOCTYPE html>
<html lang="en">
<head>
<meta charset="utf-8">
<title>QV Holdings — Actuarial Software</title>
<link rel="stylesheet" href="https://fonts.googleapis.com/css2?family=Krona+One&family=Open+Sans:wght@400;500;600&display=swap">
<style>
:root{
  --blue:#1547f2;
  --blue-soft:#e9eefc;
  --orange:#f2701e;
  --orange-soft:#fbe8d2;
  --ink:#121826;
  --text:#2b2f3a;
  --muted:#5a6070;
  --card:#f2f2f3;
  --navy:#1b2b47;
  --green:#6fb56a;
  --line:#c9ced8;
}
*{box-sizing:border-box;margin:0;padding:0}
html,body{width:1200px;height:3531px;overflow:hidden;background:#fff}
body{position:relative;font-family:"Open Sans",sans-serif;color:var(--text)}
.display{font-family:"Krona One",sans-serif;color:var(--ink);font-weight:400;letter-spacing:.5px}
.abs{position:absolute}
.link{color:var(--blue);font-size:11px;display:inline-flex;align-items:center;gap:6px}
.btn{display:inline-flex;align-items:center;gap:10px;background:var(--blue);color:#fff;border-radius:22px;font-size:15px;padding:0 18px;height:44px}

/* hero */
.hero{left:19px;top:0;width:1162px;height:643px;border-radius:0 0 36px 36px;overflow:hidden;
  background:
   radial-gradient(circle at 0% 0%,#a9b4f2 0,rgba(169,180,242,0) 45%),
   radial-gradient(circle at 0% 100%,#8c9cf0 0,rgba(140,156,240,0) 45%),
   radial-gradient(circle at 100% 100%,#62ae5e 0,rgba(98,174,94,0) 45%),
   radial-gradient(circle at 100% 0%,#d9e8f7 0,rgba(217,232,247,0) 40%),
   linear-gradient(120deg,#dfe3fb,#f4efe9 50%,#e2efe0)}
.logo{font-size:19px;color:var(--ink);display:flex;align-items:center;gap:8px;letter-spacing:1px}
.logo .dot{width:12px;height:12px;border-radius:50%;background:var(--orange)}
.nav{left:348px;top:31px;display:flex;gap:23px;font-size:15px;color:var(--ink)}
.nav .on{color:var(--blue)}
.login{left:960px;top:23px;width:108px;height:30px;border:1px solid #333;border-radius:16px;font-size:12px;display:flex;align-items:center;justify-content:center;color:var(--ink)}
.hero h1{left:93px;top:196px;font-size:41px;line-height:47px;width:640px}
.hero h1 em{font-style:normal;color:var(--orange)}
.hero .lead{left:93px;top:354px;width:500px;font-size:15px;line-height:21px;color:#222}
.hero .btn{left:93px;top:413px}

/* section generic */
.sec-title{font-size:31px;line-height:40px}
.sec-lead{font-size:15px;line-height:20px;color:var(--text)}

.feature{top:858px;width:238px;height:284px;background:var(--card);border-radius:4px;padding:20px 12px}
.feature h3{font-size:15px;font-weight:500;color:var(--ink)}
.feature .ic{margin-top:18px}
.feature p{position:absolute;left:12px;right:12px;bottom:18px;font-size:11px;line-height:15px;color:#333}
.feature.hot{background:linear-gradient(150deg,#f4f4f4 35%,#fcd8b6 75%,#f78a35)}
.feature.hot p{bottom:46px}
.feature.hot .link{position:absolute;left:12px;bottom:14px}
.ic{width:62px;height:62px;border-radius:50%;background:#fff;box-shadow:0 0 0 4px #e3e8fb;display:flex;align-items:center;justify-content:center}
.ic.warm{background:#fde9d8;box-shadow:0 0 0 4px #fff}

.watermark{left:100px;top:1212px;font-size:94px;color:#e6ebfb;letter-spacing:6px;white-space:nowrap}
.core{left:19px;top:1298px;width:1162px;height:502px;border-radius:24px;background:linear-gradient(180deg,#e9eefc 0,#eef2fb 60%,#dff0ec)}
.sol{top:1463px;height:275px;background:#fff;border-radius:12px;padding:40px 52px}
.sol h3{font-size:20px;font-weight:500;color:var(--ink);letter-spacing:.5px}
.sol p{font-size:12px;line-height:17px;margin-top:18px}
.sol ul{list-style:none;margin-top:18px;font-size:11px;line-height:17px}
.sol li::before{content:"";display:inline-block;width:7px;height:7px;border:1.5px solid var(--orange);border-radius:50%;margin-right:6px}
.sol.fade{color:#b7bcc8;opacity:.9}
.sol.fade h3{color:#8d93a3}
.sol.fade li::before{border-color:#c7ccd6}
.sol.main{background:linear-gradient(155deg,#fff 40%,#fde0c6 78%,#f78a35);border:2px solid #dfe6fb;box-shadow:0 4px 16px rgba(60,80,160,.12)}
.sol.main .link{margin-top:22px}

.char{width:341px;display:flex;gap:16px}
.char h4{font-size:16px;font-weight:500;color:var(--ink)}
.char p{font-size:11px;line-height:15px;margin-top:6px;color:#444}
.char .ic{flex:none;width:58px;height:58px}
.divider{height:1px;background:var(--line)}
.emblem{left:483px;top:1985px;width:233px;height:261px;border-radius:18px;
  background:radial-gradient(circle at 50% 50%,#fff 0,#eef0fb 30%,rgba(255,255,255,0) 60%),linear-gradient(140deg,#9fb0f2,#eef3f6 50%,#6fb56a)}

.post{border:1px solid var(--orange);border-radius:12px;left:112px;top:2431px;width:469px;height:348px;padding:17px}
.post .thumb{height:181px;border-radius:10px;background:linear-gradient(135deg,#0f2a3a 0,#133650 45%,#2344c8 85%,#1d6e5a);position:relative}
.post .stamp{position:absolute;left:46px;right:46px;bottom:0;height:28px;background:var(--orange);color:#fff;font-size:12px;display:flex;justify-content:space-between;align-items:center;padding:0 20px}
.post h4{font-size:16px;font-weight:500;color:var(--ink);margin-top:26px}
.post p{font-size:11px;line-height:15px;margin-top:12px;width:300px}
.post .link{margin-top:16px}
.brief{left:609px;width:478px;height:160px;border:1px solid var(--blue);border-radius:12px;overflow:hidden}
.brief .bar{position:absolute;left:0;top:0;width:343px;height:30px;background:var(--blue);color:#fff;font-size:12px;display:flex;justify-content:space-between;align-items:center;padding:0 20px}
.brief .act{position:absolute;top:6px;width:26px;height:26px;border:1px solid #999;border-radius:6px;display:flex;align-items:center;justify-content:center}
.brief h4{position:absolute;left:28px;top:58px;font-size:17px;font-weight:500;color:var(--ink)}
.brief p{position:absolute;left:27px;top:96px;width:320px;font-size:11px;line-height:15px}
.brief .qv{position:absolute;right:18px;bottom:-8px;font-family:"Krona One",sans-serif;font-size:44px;color:#eef1fc}

.cta{left:19px;top:2843px;width:1162px;height:372px;border-radius:30px 30px 0 0;overflow:hidden;
  background:radial-gradient(circle at 0% 0%,#2a43f0 0,rgba(42,67,240,0) 50%),radial-gradient(circle at 100% 100%,#4fa55a 0,rgba(79,165,90,0) 50%),linear-gradient(120deg,#3d5ee6,#7a95c9 45%,#7fb39b)}
.cta h2{left:93px;top:55px;width:520px;font-size:34px;line-height:50px;color:#fff}
.cta .lead{left:93px;top:172px;width:520px;font-size:15px;line-height:20px;color:#ffd6b8}
.cta .btn{left:93px;top:264px}
.field{position:absolute;background:#fff;color:#7a7f8a;font-size:12px;padding:0 14px;display:flex;align-items:center}
.send{left:650px;top:264px;width:121px;height:35px;border-radius:18px;background:var(--orange);color:#fff;font-size:15px;display:flex;align-items:center;gap:18px;padding-left:24px;border:1px solid #fff}

.footer{left:0;top:3215px;width:1200px;height:316px;background:var(--navy);color:#fff}
.footer .logo{color:#fff}
.footer h5{font-size:15px;font-weight:600}
.footer .about{left:112px;top:114px;width:265px;font-size:11.5px;line-height:15px}
.footer .col{font-size:12px;line-height:17.5px}
.footer .vline{top:48px;width:1px;height:232px;background:#5d6b86}
.crow{display:flex;gap:14px;align-items:flex-start;font-size:12px;line-height:17px}
.circ{flex:none;width:22px;height:22px;border:1px solid #fff;border-radius:50%;display:flex;align-items:center;justify-content:center}
.footer .orange{color:var(--orange)}
</style>
</head>
<body>

<section class="hero abs">
  <div class="logo abs" style="left:93px;top:28px"><span class="dot"></span>QV Holdings</div>
  <nav class="nav abs"><span class="on">Home</span><span>Platform</span><span>Solutions</span><span>Insights</span><span>Company</span><span>Contact</span></nav>
  <div class="login abs">Client Login</div>
  <h1 class="display abs">Actuarial Software For Structured, Auditable <em>Financial</em> Analysis.</h1>
  <p class="lead abs">QV Holdings Develops Software That Translates Established Actuarial Methodologies Into &nbsp;Disciplined, Decision-Ready Tools.</p>
  <span class="btn abs">Request A Technical Walkthrough
    <svg width="20" height="20" viewBox="0 0 20 20"><path d="M3 17 C10 17 16 12 16 3" stroke="#fff" stroke-width="2" fill="none"/></svg></span>
  <svg class="abs" style="left:560px;top:90px" width="520" height="500" viewBox="0 0 520 500" role="img" aria-label="QV Holdings emblem within concentric rings">
    <g fill="none" stroke="#fff" stroke-opacity=".35">
      <circle cx="319" cy="243" r="215" stroke-width="28"/>
      <circle cx="319" cy="243" r="180" stroke-width="22"/>
    </g>
    <circle cx="319" cy="243" r="150" fill="#f1f5f2" fill-opacity=".6" stroke="#d8ead0" stroke-width="2"/>
    <circle cx="319" cy="243" r="125" fill="#e6f1ea"/>
    <circle cx="319" cy="243" r="85" fill="#d8eee2"/>
    <text x="319" y="253" text-anchor="middle" font-family="Krona One, sans-serif" font-size="26" fill="#121826">QV Holdings</text>
  </svg>
</section>

<h2 class="display sec-title abs" style="left:112px;top:703px;width:470px">A Platform For Structured Actuarial Decision-Making</h2>
<p class="sec-lead abs" style="left:633px;top:706px;width:460px">QV Holdings Provides A Disciplined Software Environment Where Actuarial Models, Financial Assumptions, And Regulatory Considerations Can Be Structured, Reviewed, And Documented. The Platform Transforms Complex Actuarial Processes Into Transparent, Auditable Workflows That Support Informed Financial Decision-Making.</p>

<div class="feature abs" style="left:112px">
  <h3>Structured Workflows</h3>
  <div class="ic"><svg width="26" height="26" viewBox="0 0 26 26" fill="#1b2b47"><rect x="2" y="10" width="7" height="7"/><rect x="17" y="3" width="7" height="6"/><rect x="17" y="17" width="7" height="6"/><path d="M9 13h4V6h4M13 13v7h4" stroke="#1b2b47" stroke-width="1.6" fill="none"/></svg></div>
  <p>Model Development And Financial Analysis Follow Clearly Defined Processes That Promote Consistency, Discipline, And Traceability.</p>
</div>
<div class="feature hot abs" style="left:358px">
  <h3>Transparent Assumptions</h3>
  <div class="ic warm"><svg width="28" height="28" viewBox="0 0 28 28"><circle cx="14" cy="12" r="7" fill="#f2701e"/><rect x="10.5" y="19" width="7" height="5" rx="1" fill="#1b2b47"/><path d="M14 1v3M3 12h3M22 12h3M6 4l2 2M22 4l-2 2" stroke="#f2701e" stroke-width="1.6"/></svg></div>
  <p>Every Input, Assumption, And Methodology Is Documented And Visible, Enabling Teams To Understand How Results Are Produced.</p>
  <span class="link">Learn More <svg width="20" height="6"><path d="M0 3h18l-3-2M18 3l-3 2" stroke="#1547f2" fill="none"/></svg></span>
</div>
<div class="feature abs" style="left:603px">
  <h3>Auditability</h3>
  <div class="ic"><svg width="26" height="26" viewBox="0 0 26 26" fill="none" stroke="#1b2b47" stroke-width="1.8"><path d="M5 3h11l4 4v15H5z"/><circle cx="13" cy="14" r="4"/><path d="M16 17l4 4"/></svg></div>
  <p>All Calculations And Changes Are Recorded, Creating A Complete And Reviewable Audit Trail For Internal Governance And External Oversight.</p>
</div>
<div class="feature abs" style="left:849px">
  <h3>Governance Support</h3>
  <div class="ic"><svg width="26" height="26" viewBox="0 0 26 26" fill="none" stroke="#1b2b47" stroke-width="1.8"><circle cx="14" cy="8" r="4"/><path d="M14 2v2M14 12v2M8 8h2M18 8h2"/><path d="M2 18h5l4 2h6l6-4M2 23h18"/></svg></div>
  <p>Built-In Structures Help Organizations Maintain Oversight Across Teams, Jurisdictions, And Regulatory Requirements.</p>
</div>

<div class="watermark display abs">QV HOLDINGS</div>
<section class="core abs"></section>
<h2 class="display sec-title abs" style="left:112px;top:1354px;width:420px">Core Actuarial Solutions</h2>
<p class="sec-lead abs" style="left:647px;top:1361px;width:450px">QV Holdings Software Supports Key Actuarial Functions Across The Insurance And Financial Services Landscape, Enabling Structured Modeling And Analysis Across Multiple Disciplines.</p>

<div class="sol fade abs" style="left:19px;width:324px;padding-left:22px;border-radius:0 12px 12px 0">
  <h3>Reserving &amp; Valuation</h3>
  <p>Designed To Support Actuarial Reserving Analysis And Valuation Processes, With Structured Workflows For Assumptions And Ensure Transparency.</p>
  <ul><li>Reserve Model Management</li><li>Reserve Scenario Analysis</li><li>Auditable Calculation Structures</li></ul>
</div>
<div class="sol main abs" style="left:362px;width:474px">
  <h3>PRICING</h3>
  <p>Enable Disciplined Pricing Analysis With Software That Supports Transparent Assumption Setting, Model Governance, And Comparative Scenario Evaluation.</p>
  <ul><li>Pricing Model Structures</li><li>Scenario Comparison</li><li>Assumption Documentation</li></ul>
  <span class="link">Learn More <svg width="20" height="6"><path d="M0 3h18l-3-2M18 3l-3 2" stroke="#1547f2" fill="none"/></svg></span>
</div>
<div class="sol fade abs" style="left:857px;width:324px;border-radius:12px 0 0 12px;white-space:nowrap;overflow:hidden">
  <h3>Enterprise Risk Management</h3>
  <p style="white-space:normal;width:260px">Support Enterprise-Level Risk Analysis With Tools Helping Organizations To Assess Financial Exposures, Scenarios, And Maintain Governance Oversight.</p>
  <ul><li>Risk Modeling Support</li><li>Stress Testing Scenarios</li><li>Enterprise Risk Documentation</li></ul>
</div>

<h2 class="display sec-title abs" style="left:112px;top:1862px;width:400px">Platform Characteristics</h2>
<p class="sec-lead abs" style="left:675px;top:1869px;width:420px">Key Capabilities Designed To Support Structured Actuarial Analysis, Transparency, And Governance Across Complex Financial Environments.</p>

<div class="char abs" style="left:112px;top:2023px">
  <div class="ic"><svg width="24" height="24" viewBox="0 0 26 26" fill="#1b2b47"><rect x="2" y="10" width="7" height="7"/><rect x="17" y="3" width="7" height="6"/><rect x="17" y="17" width="7" height="6"/><path d="M9 13h4V6h4M13 13v7h4" stroke="#1b2b47" stroke-width="1.6" fill="none"/></svg></div>
  <div><h4>Structured Workflows</h4><p>Clearly Defined Modeling Processes That Promote Consistency And Disciplined Analysis.</p></div>
</div>
<div class="divider abs" style="left:112px;top:2116px;width:341px"></div>
<div class="char abs" style="left:112px;top:2145px">
  <div class="ic"><svg width="24" height="24" viewBox="0 0 24 24" fill="#1b2b47"><rect x="3" y="12" width="18" height="10"/><circle cx="8" cy="6" r="2.5"/><circle cx="16" cy="6" r="2.5"/><path d="M12 2l1 2h2l-1.6 1.2.6 2L12 6l-2 1.2.6-2L9 4h2z"/></svg></div>
  <div><h4>Multi-Jurisdictional Review Support</h4><p>Supports Review And Analysis Across Different Regulatory And Reporting Environments.</p></div>
</div>

<div class="emblem abs" role="img" aria-label="QV Holdings emblem on a soft gradient tile">
  <svg width="233" height="261" viewBox="0 0 233 261">
    <circle cx="117" cy="130" r="95" fill="none" stroke="#fff" stroke-opacity=".5" stroke-width="18"/>
    <circle cx="117" cy="130" r="62" fill="#eef5f0" stroke="#cfe8cf" stroke-width="2"/>
    <text x="117" y="136" text-anchor="middle" font-family="Krona One, sans-serif" font-size="15" fill="#121826">QV Holdings</text>
  </svg>
</div>

<div class="char abs" style="left:746px;top:2023px">
  <div class="ic"><svg width="26" height="26" viewBox="0 0 28 28"><circle cx="14" cy="12" r="7" fill="#1b2b47"/><rect x="10.5" y="19" width="7" height="5" rx="1" fill="#1b2b47"/><path d="M14 1v3M3 12h3M22 12h3" stroke="#1b2b47" stroke-width="1.6"/></svg></div>
  <div><h4>Transparent Assumptions</h4><p>All Inputs And Assumptions Are Visible And Documented For Clarity And Oversight.</p></div>
</div>
<div class="divider abs" style="left:746px;top:2116px;width:341px"></div>
<div class="char abs" style="left:746px;top:2145px">
  <div class="ic"><svg width="26" height="26" viewBox="0 0 26 26" fill="none" stroke="#1b2b47" stroke-width="1.8"><circle cx="12" cy="12" r="9"/><path d="M6 15l4-4 3 3 5-6"/><path d="M18 18l5 5"/></svg></div>
  <div><h4>Comparative Analysis Capability</h4><p>Evaluate Multiple Scenarios Side-By-Side To Understand The Impact Of Different Assumptions.</p></div>
</div>

<h2 class="display sec-title abs" style="left:112px;top:2314px;width:380px">Insights &amp; Perspectives</h2>
<p class="sec-lead abs" style="left:649px;top:2321px;width:445px">Articles And Perspectives Exploring Actuarial Methodologies, Financial Governance, And The Challenges Of Working Across Complex Regulatory Environments.</p>

<article class="post abs">
  <div class="thumb" role="img" aria-label="Illustration of a rising financial chart arrow on a dark background">
    <div class="stamp"><span>Friday, May 24</span><span>7:00 PM</span></div>
  </div>
  <h4>Actuarial Methods</h4>
  <p>Perspectives On Established Methodologies And Their Application In Modern Financial Analysis.</p>
  <span class="link">Learn More <svg width="20" height="6"><path d="M0 3h18l-3-2M18 3l-3 2" stroke="#1547f2" fill="none"/></svg></span>
</article>

<article class="brief abs" style="top:2431px">
  <div class="bar"><span>Friday, May 24</span><span>7:00 PM</span></div>
  <span class="act" style="left:359px"><svg width="14" height="13" viewBox="0 0 14 13"><path d="M7 12L1.5 6.5A3.2 3.2 0 017 2.5a3.2 3.2 0 015.5 4z" fill="none" stroke="#222" stroke-width="1.2"/></svg></span>
  <span class="act" style="left:402px"><svg width="14" height="14" viewBox="0 0 14 14" fill="none" stroke="#222" stroke-width="1.2"><path d="M9 1h4v4M13 1L7 7M11 8v5H1V3h5"/></svg></span>
  <h4>Governance In Financial Modeling</h4>
  <p>Insights On Transparency, Oversight, And Disciplined Model Management.</p>
  <span class="qv">QV</span>
</article>
<article class="brief abs" style="top:2620px">
  <div class="bar"><span>Friday, May 24</span><span>7:00 PM</span></div>
  <span class="act" style="left:359px"><svg width="14" height="13" viewBox="0 0 14 13"><path d="M7 12L1.5 6.5A3.2 3.2 0 017 2.5a3.2 3.2 0 015.5 4z" fill="none" stroke="#222" stroke-width="1.2"/></svg></span>
  <span class="act" style="left:402px"><svg width="14" height="14" viewBox="0 0 14 14" fill="none" stroke="#222" stroke-width="1.2"><path d="M9 1h4v4M13 1L7 7M11 8v5H1V3h5"/></svg></span>
  <h4>Multi-Jurisdictional Practice</h4>
  <p>Discussion Of Actuarial Work Across Different Regulatory And Reporting Environments.</p>
  <span class="qv">QV</span>
</article>

<section class="cta abs">
  <h2 class="display abs">Request A Technical Walkthrough</h2>
  <p class="lead abs">Explore How QV Holdings' Software Supports Structured Actuarial Workflows, Transparent Assumptions, And Auditable Financial Analysis. Request A Technical Walkthrough To See How The Platform Can Support Your Organization's Analytical And Governance Needs.</p>
  <span class="btn abs">Request A Technical Walkthrough
    <svg width="20" height="20" viewBox="0 0 20 20"><path d="M3 17 C10 17 16 12 16 3" stroke="#fff" stroke-width="2" fill="none"/></svg></span>
  <div class="field" style="left:650px;top:88px;width:203px;height:36px">First Name</div>
  <div class="field" style="left:865px;top:88px;width:203px;height:36px">Last Name</div>
  <div class="field" style="left:650px;top:139px;width:203px;height:37px">Email ID</div>
  <div class="field" style="left:865px;top:139px;width:203px;height:37px">Phone Number</div>
  <div class="field" style="left:650px;top:190px;width:418px;height:60px;align-items:flex-start;padding-top:12px">Message (required)</div>
  <div class="send abs">Send <svg width="18" height="18" viewBox="0 0 20 20"><path d="M3 17 C10 17 16 12 16 3" stroke="#fff" stroke-width="2" fill="none"/></svg></div>
</section>

<footer class="footer abs">
  <div class="logo abs" style="left:112px;top:52px;font-size:22px"><span class="dot"></span>QV Holdings</div>
  <p class="about abs">QV Holdings develops actuarial software designed to support structured financial analysis, transparent assumptions, and auditable modeling workflows. The platform helps actuaries and financial professionals apply established methodologies within disciplined, governance-focused environments.</p>
  <div class="vline abs" style="left:393px"></div>
  <div class="abs col" style="left:440px;top:66px">
    <h5>Quick Links</h5>
    <div style="margin-top:12px">Accueil<br>À propos<br>Services<br>Fonctionnement<br>Témoignages<br>Questions fréquentes<br>Contact</div>
  </div>
  <div class="abs" style="left:648px;top:66px">
    <h5>Contact Info</h5>
    <div class="crow" style="margin-top:12px"><span class="circ"><svg width="10" height="12" viewBox="0 0 10 12"><path d="M5 11S1 6.5 1 4.2a4 4 0 018 0C9 6.5 5 11 5 11z" fill="none" stroke="#fff"/><circle cx="5" cy="4.3" r="1.3" fill="#fff"/></svg></span><span>410 Meridian Park Ave, Suite 12<br>Harbor City, ST 00000</span></div>
    <div class="crow" style="margin-top:14px"><span class="circ"><svg width="11" height="11" viewBox="0 0 11 11"><path d="M2 1l2 .3.8 2.2-1.2.9a6 6 0 003 3l.9-1.2 2.2.8.3 2c-4 1-9-4-8-8z" fill="#fff"/></svg></span><span>+1(555)010-0192</span></div>
    <div class="orange" style="margin-top:12px;font-size:12px">contact@qv-holdings.example</div>
    <div class="orange" style="margin-top:10px;font-size:12px">www.qv-holdings.example</div>
  </div>
  <div class="vline abs" style="left:939px"></div>
  <div class="abs" style="left:986px;top:66px">
    <h5>Social Media</h5>
    <div class="crow" style="margin-top:12px;align-items:center;font-size:11px"><span class="circ"></span>Friendsphere</div>
    <div class="crow" style="margin-top:18px;align-items:center;font-size:11px"><span class="circ"></span>Chirper</div>
    <div class="crow" style="margin-top:18px;align-items:center;font-size:11px"><span class="circ"></span>ProNet</div>
  </div>
  <div class="abs" style="left:112px;top:258px;width:975px;height:1px;background:#5d6b86"></div>
  <div class="abs" style="left:0;top:277px;width:1200px;text-align:center;font-size:12px">Copyright &amp;Copy; 2026 . All Rights Reserved.Legal Mentions</div>
</footer>

</body>
</html>
```